Business Card Design

I am a golf mind and performance coach. I teach several programs. The Steady Arc Method program and The Calm Edge program. I hold a certificate in Golf Psychology Coaching also. The design should highlight both programs I coach - one on either side - and also the fact I hold a certificate in Golf Psychology coaching.

Target Market(s)

golfers

Industry/Entity Type

Business

Contact Information for Business Card

Brian Hollow
Golf Mind & Performance Coach
Ph UK 07922431875
Ph New Zealand 0219637215
Email: brian@stillgreenputt.co.uk
Web: www.stillgreenputt.co.uk

```html
<!DOCTYPE html>
<html lang="en">
<head>
<meta charset="utf-8">
<title>The Steady Arc Method and The Calm Edge – Business Card</title>
<link href="https://fonts.googleapis.com/css2?family=Jost:wght@500&family=Marcellus&family=Open+Sans:wght@400;700&display=swap" rel="stylesheet">
<style>
  :root {
    --navy: #233a5a;
    --gold: #f7b035;
    --white: #ffffff;
    --ink: #2b3440;
    --divider: #c9ccd1;
    --backdrop: #e9e7e4;
  }
  * { box-sizing: border-box; margin: 0; padding: 0; }
  html, body {
    width: 1200px; height: 1200px; overflow: hidden;
    background: var(--backdrop);
  }
  .sheet { position: relative; width: 1200px; height: 1200px; }
  .card {
    position: absolute; left: 180px; width: 840px; height: 480px;
    background: var(--white); border-radius: 28px; overflow: hidden;
    box-shadow: 0 6px 18px rgba(0,0,0,0.15);
  }
  .card--front { top: 70px; }
  .card--back { top: 650px; }

  .brand {
    position: absolute; left: 50px; top: 140px; width: 370px;
    text-align: center;
  }
  .brand__mark {
    width: 64px; height: 64px; border-radius: 50%;
    background: var(--navy); margin: 0 auto 22px;
  }
  .brand__name {
    font-family: "Jost", sans-serif; font-weight: 500;
    font-size: 29px; color: var(--navy); white-space: nowrap;
  }
  .brand__tagline {
    font-family: "Marcellus", serif; font-size: 21px;
    color: var(--navy); margin-top: 10px; white-space: nowrap;
  }
  .divider {
    position: absolute; left: 448px; top: 160px; width: 1px; height: 150px;
    background: var(--divider);
  }
  .contacts {
    position: absolute; left: 470px; top: 158px; list-style: none;
    font-family: "Open Sans", sans-serif; font-size: 19px; color: var(--ink);
  }
  .contacts li { display: flex; align-items: center; height: 35px; }
  .contacts svg { width: 17px; height: 17px; margin-right: 8px; flex: none; }

  .swoosh { position: absolute; left: 0; top: 0; width: 840px; height: 480px; }

  .holder {
    position: absolute; right: 40px; top: 372px; width: 330px;
    text-align: center; color: var(--white); font-family: "Open Sans", sans-serif;
  }
  .holder__name { font-weight: 700; font-size: 27px; }
  .holder__role { font-size: 18px; margin-top: 4px; }

  .back-brand {
    position: absolute; left: 0; right: 0; top: 60px; text-align: center;
  }
  .back-brand__mark {
    width: 150px; height: 150px; border-radius: 50%;
    background: var(--navy); margin: 0 auto 24px;
  }
  .back-brand__name {
    font-family: "Jost", sans-serif; font-weight: 500;
    font-size: 34px; color: var(--navy);
  }
  .back-brand__credential {
    font-family: "Marcellus", serif; font-size: 20px;
    color: var(--navy); margin-top: 8px;
  }
  .back-url {
    position: absolute; left: 0; right: 0; top: 392px; text-align: center;
    font-family: "Open Sans", sans-serif; font-size: 27px;
    letter-spacing: 3px; color: var(--ink);
  }
</style>
</head>
<body>
<main class="sheet">

  <section class="card card--front">
    <svg class="swoosh" viewBox="0 0 840 480" aria-hidden="true">
      <path d="M0,412 C260,370 560,320 840,352 L840,480 L0,480 Z" fill="var(--navy)"/>
      <path d="M0,426 C260,388 540,346 840,368" fill="none" stroke="var(--white)" stroke-width="8"/>
      <path d="M0,438 C260,420 430,396 580,356 C460,430 270,468 80,480 L0,480 Z" fill="var(--white)"/>
      <path d="M0,446 C230,434 420,404 570,360 C450,436 260,472 70,480 L0,480 Z" fill="var(--gold)"/>
    </svg>

    <div class="brand">
      <div class="brand__mark"></div>
      <div class="brand__name">The Steady Arc Method</div>
      <div class="brand__tagline">A Revolutionary Golf Program</div>
    </div>

    <div class="divider"></div>

    <ul class="contacts">
      <li>
        <svg viewBox="0 0 16 16"><circle cx="8" cy="8" r="7" fill="none" stroke="var(--navy)" stroke-width="1.4"/><path d="M6,4.5 L7.2,6.6 L6.4,7.4 C6.9,8.5 7.6,9.2 8.6,9.7 L9.4,8.9 L11.5,10 L10.8,11.6 C8,11.6 4.5,8 4.5,5.2 Z" fill="var(--navy)"/></svg>
        07922431875(UK)
      </li>
      <li>
        <svg viewBox="0 0 16 16"><circle cx="8" cy="8" r="7" fill="none" stroke="var(--navy)" stroke-width="1.4"/><path d="M6,4.5 L7.2,6.6 L6.4,7.4 C6.9,8.5 7.6,9.2 8.6,9.7 L9.4,8.9 L11.5,10 L10.8,11.6 C8,11.6 4.5,8 4.5,5.2 Z" fill="var(--navy)"/></svg>
        0219637215(NZ)
      </li>
      <li>
        <svg viewBox="0 0 16 16"><rect x="1.5" y="4" width="13" height="9" rx="1" fill="var(--navy)"/><path d="M1.5,4.5 L8,9 L14.5,4.5" fill="none" stroke="var(--white)" stroke-width="1.2"/></svg>
        brian@stillgreenputt.co.uk
      </li>
      <li>
        <svg viewBox="0 0 16 16"><circle cx="8" cy="8" r="6.5" fill="var(--navy)"/><path d="M1.5,8 H14.5 M8,1.5 V14.5 M8,1.5 C4.5,5 4.5,11 8,14.5 M8,1.5 C11.5,5 11.5,11 8,14.5" fill="none" stroke="var(--white)" stroke-width="0.9"/></svg>
        www.stillgreenputt.co.uk
      </li>
    </ul>

    <div class="holder">
      <div class="holder__name">Brian Hollow</div>
      <div class="holder__role">Golf Mind &amp; Performance Coach</div>
    </div>
  </section>

  <section class="card card--back">
    <div class="back-brand">
      <div class="back-brand__mark"></div>
      <div class="back-brand__name">The Calm Edge</div>
      <div class="back-brand__credential">Certified in Golf Psychology Coaching</div>
    </div>
    <div class="back-url">www.stillgreenputt.co.uk</div>
  </section>

</main>
</body>
</html>
```